business card with 2 locations on 1 card

I need a modern looking business card that I would use at 2 different locations. Possibly 1 location on 1 side and other location on other side. One should be able to distinguish the 2 locations immediately before having to read the address or description on card. You can take a look at my website to see what I'm drawn to. The logo is brand new that I just purchased on Pixel Harbor. I want to emphasize family.
Updates

Let's not use the yellow and blue colors. Added Thursday, August 31, 2017

Target Market(s)

women and children

Industry/Entity Type

Health And Wellness

Contact Information for Business Card

Business name: Willow Nest Chiropractic & Acupuncture
My name: Delsa Brook
Job title: DC, MAOM, LAc (CA), CNS

Location 1
Address: 4817 Marlowe Blvd, Suite C-200, Frisco, TX 75036
Phone: (469) 555-0182
Fax: (972) 555-0147

Location 2
Address: 1786 Tenley Road, Suite 300, Plano, TX 75079
Phone: (469) 555-0195
Fax: (972) 555-0147

Email: drdelsabrook@mailvex.example
Website: www.drdelsabrook.example

Font styles to use
Serif
Sans Serif

Colors

Designer to choose colors to be used in the design.

Requirements
Must have
• distinction between 2 locations.
Nice to have
• Colors preference below is there. But I like to see what you come up with too!

```html
<!DOCTYPE html>
<html lang="en">
<head>
<meta charset="utf-8">
<title>Willow Nest Chiropractic &amp; Acupuncture – Business Card</title>
<link href="https://fonts.googleapis.com/css2?family=Questrial&display=swap" rel="stylesheet">
<style>
  :root {
    --teal-deep: #2a7472;
    --teal-text: #3f7f80;
    --aqua: #5ec8d3;
    --cream: #f4f1d0;
    --white: #ffffff;
    --charcoal: #3d3d3f;
    --text-grey: #6a6a6c;
    --stage: #e9e9ea;
  }
  * { box-sizing: border-box; margin: 0; padding: 0; }
  html, body { width: 1200px; height: 879px; overflow: hidden; }
  body {
    background: var(--stage);
    font-family: "Questrial", "Century Gothic", sans-serif;
    color: var(--text-grey);
    position: relative;
  }
  .card {
    position: absolute;
    width: 500px;
    height: 286px;
    box-shadow: 0 6px 18px rgba(0,0,0,.15);
    overflow: hidden;
  }
  .card--front { left: 70px; top: 270px; background: var(--white); }
  .card--back  { left: 630px; top: 270px; background: var(--cream); }

  .band { position: absolute; height: 11px; }
  .band--top-aqua { top: 0; left: 0; width: 68%; background: var(--aqua); }
  .band--top-cream { top: 0; right: 0; width: 32%; background: var(--cream); }
  .band--bottom-cream { bottom: 0; left: 0; width: 38%; background: var(--cream); }
  .band--bottom-aqua { bottom: 0; right: 0; width: 62%; background: var(--aqua); }

  .holder { position: absolute; left: 32px; top: 30px; }
  .holder__name { font-size: 21px; color: var(--teal-text); font-weight: 700; }
  .holder__title { font-size: 11.5px; margin-top: 4px; letter-spacing: .3px; }

  .contact { position: absolute; left: 32px; top: 96px; font-size: 11.5px; line-height: 19px; }
  .contact__row { display: flex; align-items: center; gap: 8px; }
  .contact__icon { width: 11px; height: 11px; flex: none; }

  .office { position: absolute; font-size: 11px; line-height: 15.5px; }
  .office__label { color: var(--teal-text); font-weight: 700; font-size: 12px; margin-bottom: 2px; }
  .office--frisco { left: 32px; top: 152px; }
  .office--plano { left: 282px; top: 176px; }
  .divider {
    position: absolute; left: 262px; top: 166px; height: 80px;
    border-left: 1.5px dotted #8a8a8a;
  }

  .brand { position: absolute; text-align: center; }
  .brand__mark { display: block; margin: 0 auto; }
  .brand__name { color: var(--teal-deep); font-family: "Questrial", sans-serif; line-height: 1.15; }
  .card--front .brand { right: 26px; top: 42px; width: 160px; }
  .card--front .brand__name { font-size: 13.5px; margin-top: 8px; }
  .card--back .brand { left: 50%; top: 50%; width: 320px; transform: translate(-50%, -50%); }
  .card--back .brand__name { font-size: 24px; margin-top: 14px; }

  .palette { position: absolute; left: 150px; top: 660px; display: flex; gap: 10px; }
  .palette__chip { width: 27px; height: 27px; border: 1px solid #bdbdbd; }
  .palette__chip--teal { background: var(--teal-deep); }
  .palette__chip--aqua { background: var(--aqua); }
  .palette__chip--cream { background: var(--cream); }
  .palette__chip--white { background: var(--white); }
  .palette__chip--charcoal { background: var(--charcoal); }
</style>
</head>
<body>

<section class="card card--front" aria-label="Card front">
  <div class="band band--top-aqua"></div>
  <div class="band band--top-cream"></div>
  <div class="band band--bottom-cream"></div>
  <div class="band band--bottom-aqua"></div>

  <div class="holder">
    <h1 class="holder__name">Delsa Brook</h1>
    <p class="holder__title">DC, MAOM, LAc (CA), CNS</p>
  </div>

  <div class="contact">
    <div class="contact__row">
      <svg class="contact__icon" viewBox="0 0 12 12"><circle cx="6" cy="6" r="6" fill="var(--charcoal)"/><rect x="3" y="4" width="6" height="4" fill="none" stroke="#fff" stroke-width="0.9"/><path d="M3 4 L6 6.3 L9 4" fill="none" stroke="#fff" stroke-width="0.9"/></svg>
      <span>drdelsabrook@mailvex.example</span>
    </div>
    <div class="contact__row">
      <svg class="contact__icon" viewBox="0 0 12 12"><circle cx="6" cy="6" r="6" fill="var(--charcoal)"/><path d="M4.5 3.5 L7.5 6 L4.5 8.5" fill="none" stroke="#fff" stroke-width="1.2"/></svg>
      <span>www.drdelsabrook.example</span>
    </div>
  </div>

  <div class="office office--frisco">
    <p class="office__label">Frisco's Office</p>
    <p>A: 4817 Marlowe Blvd, Suite C-200,</p>
    <p>Frisco, TX 75036</p>
    <p>Phone: (469) 555-0182</p>
    <p>Fax: (972) 555-0147</p>
  </div>

  <div class="divider"></div>

  <div class="office office--plano">
    <p class="office__label">Plano's Office</p>
    <p>A: 1786 Tenley Road, Suite 300,</p>
    <p>Plano, TX 75079</p>
    <p>Phone: (469) 555-0195</p>
    <p>Fax: (972) 555-0147</p>
  </div>

  <div class="brand">
    <svg class="brand__mark" width="56" height="56" viewBox="0 0 56 56"><circle cx="28" cy="28" r="26" fill="none" stroke="var(--teal-deep)" stroke-width="3"/></svg>
    <p class="brand__name">Willow Nest Chiropractic &amp; Acupuncture</p>
  </div>
</section>

<section class="card card--back" aria-label="Card back">
  <div class="brand">
    <svg class="brand__mark" width="96" height="96" viewBox="0 0 96 96"><circle cx="48" cy="48" r="45" fill="none" stroke="var(--teal-deep)" stroke-width="4"/></svg>
    <p class="brand__name">Willow Nest Chiropractic &amp; Acupuncture</p>
  </div>
</section>

<div class="palette" aria-label="Colour palette">
  <div class="palette__chip palette__chip--teal"></div>
  <div class="palette__chip palette__chip--aqua"></div>
  <div class="palette__chip palette__chip--cream"></div>
  <div class="palette__chip palette__chip--white"></div>
  <div class="palette__chip palette__chip--charcoal"></div>
</div>

</body>
</html>
```